Cover page for Master's thesis (in Word)

I need a cover page for my Master's thesis which I am currently working on. The topic is "Mobile Usability" so MOBILE should also be the overall theme of the design. The primary color should be blue since my school and the company where I am writing my thesis are primarily using blue in their Corporate Identities.
I enclosed a template in Word and pdf with all the necessary information that must be included on the cover page. Please also consider and adhere to the page margins and the printable areas set in the Word template and please use Verdana for the mandatory text elements mentioned. The topic font can be different and it's up to you.
The design shouldn't be too fancy since this is a dissertation and not an ad for an Quillion product. I would prefer a simple, flat, modern and professional design with flat colors. I also attached the logo of my University and my company (which should of course be included) as well as a leaflet of my Uni for inspiration.

If you have any questions or if you need more information or material, just drop me a line.

Thanks a lot in advance!
Matthias

```html
<!DOCTYPE html>
<html lang="en">
<head>
<meta charset="utf-8">
<title>Master's Thesis Cover – Mobile Usability</title>
<link rel="stylesheet" href="https://fonts.googleapis.com/css2?family=Noto+Sans:wght@400;700&family=Archivo+Black&family=Tinos&display=swap">
<style>
  :root {
    --blue-deep: #1d3f86;
    --blue-mid: #3563b0;
    --blue-light: #8fb1e3;
    --blue-pale: #c9dcf4;
    --logo-blue: #1f4e9c;
    --title-red: #e11b22;
    --white: #ffffff;
  }
  html, body {
    margin: 0;
    padding: 0;
    width: 851px;
    height: 1200px;
    overflow: hidden;
    background: var(--white);
  }
  .cover {
    position: relative;
    width: 851px;
    height: 1200px;
    overflow: hidden;
    background:
      radial-gradient(ellipse 520px 420px at 50% 12%, var(--blue-light) 0%, rgba(143,177,227,0) 100%),
      linear-gradient(180deg, var(--blue-mid) 0%, var(--blue-deep) 55%, var(--blue-mid) 100%);
    font-family: "Noto Sans", Verdana, sans-serif;
    color: var(--white);
  }
  .university-mark {
    position: absolute;
    left: 250px;
    top: 28px;
    width: 350px;
    height: 128px;
    background: var(--white);
    border-radius: 64px;
    display: flex;
    align-items: center;
    justify-content: center;
    gap: 16px;
    box-sizing: border-box;
    padding: 0 28px;
  }
  .university-mark .dot {
    width: 28px;
    height: 28px;
    border-radius: 50%;
    background: var(--logo-blue);
    flex: none;
  }
  .university-mark .name {
    font-family: "Noto Sans", Verdana, sans-serif;
    font-weight: 400;
    font-size: 25px;
    line-height: 1.2;
    color: var(--logo-blue);
  }
  .thesis-kind {
    position: absolute;
    left: 94px;
    top: 252px;
    margin: 0;
    font-family: "Archivo Black", sans-serif;
    font-size: 21px;
    line-height: 28px;
    letter-spacing: 0.5px;
    color: var(--white);
  }
  .thesis-title {
    position: absolute;
    left: 86px;
    top: 290px;
    width: 680px;
    height: 92px;
    margin: 0;
    background: var(--white);
    text-align: center;
    font-family: "Archivo Black", sans-serif;
    font-weight: 400;
    font-size: 72px;
    line-height: 90px;
    white-space: nowrap;
    color: var(--title-red);
  }
  .thesis-subtitle {
    position: absolute;
    left: 0;
    right: 0;
    top: 396px;
    margin: 0;
    text-align: center;
    font-family: "Tinos", serif;
    font-size: 31px;
    line-height: 44px;
    color: var(--white);
  }
  .details {
    position: absolute;
    left: 85px;
    top: 505px;
    border-collapse: collapse;
    font-size: 25px;
    line-height: 48px;
  }
  .details th {
    width: 346px;
    font-weight: 400;
    text-align: left;
    padding: 0;
    white-space: nowrap;
  }
  .details td {
    padding: 0;
    white-space: nowrap;
  }
  .background-pattern {
    position: absolute;
    left: 0;
    bottom: 0;
    width: 851px;
    height: 470px;
    background: linear-gradient(180deg, rgba(201,220,244,0) 0%, rgba(201,220,244,0.35) 60%, rgba(201,220,244,0.55) 100%);
  }
  .mobile-illustration {
    position: absolute;
    left: 582px;
    top: 936px;
    width: 256px;
    height: 240px;
    border-radius: 18px;
    background: radial-gradient(circle at 35% 30%, #f7c63c 0%, #8cc63f 45%, #2f5f3a 100%);
  }
</style>
</head>
<body>
<main class="cover">
  <div class="background-pattern" role="img" aria-label="Soft pattern of light blue squares fading across the lower page"></div>

  <div class="university-mark">
    <span class="dot"></span>
    <span class="name">Northfield Technical University</span>
  </div>

  <p class="thesis-kind">MASTER'S THESIS</p>
  <h1 class="thesis-title">Mobile Usability</h1>
  <p class="thesis-subtitle">Analysis of the mobile application<br>portfolio of XXXXX Ltd.</p>

  <table class="details">
    <tr><th>Surname, Name</th><td>Matthias Reinhardt</td></tr>
    <tr><th>Matriculation Number</th><td>000XXXXX</td></tr>
    <tr><th>Degree Program</th><td>Marketing / Sales / Media</td></tr>
    <tr><th>Issued on</th><td>06.11.2013</td></tr>
    <tr><th>Submitted on</th><td>07.04.2014</td></tr>
    <tr><th>First Examiner</th><td>Prof. Dr. Laura Brandt</td></tr>
    <tr><th>Second Examiner</th><td>Prof. Dr. Karl Essen</td></tr>
  </table>

  <div class="mobile-illustration" role="img" aria-label="Illustration of a smartphone with a sun and green leaves"></div>
</main>
</body>
</html>
```